Web Design for One for One Organic Soap Company

We need a website design for the company Tidewell Botanics based on the package design per attached.

The design should communicate high end, luxury organic. The site will provide facts about how the spread of disease causes deaths and can be prevented with hand washing. The site will also have a page about why we are passionate about organics and how that relates to our skin including skin facts.
Also, the site should have an e-commerce product page and shopping cart.

Target Market(s)

Educated, health conscious and socially conscious consumers who shop luxury. Target vendors include Larkmont Grocers and Velbrook..

Industry/Entity Type

E-Commerce

Font styles to use
Other font styles liked:
• See attached

Requirements
Must have
• Use of Ying Yang leaf Logo provided.
Based on design provided.

```html
<!DOCTYPE html>
<html lang="en">
<head>
<meta charset="utf-8">
<title>Tidewell Botanics – Organic Soap</title>
<link rel="stylesheet" href="https://fonts.googleapis.com/css2?family=Open+Sans:wght@400;600;700&family=Great+Vibes&family=Italianno&display=swap">
<style>
:root{
  --linen:#e9e2d0;
  --page:#ffffff;
  --brown:#3b2313;
  --rust:#a9391f;
  --red:#b3381c;
  --card:#e3dbc8;
  --side:#c9c9c9;
  --ink:#2b2b2b;
  --orange1:#f0a422;
  --orange2:#cf7a06;
}
*{box-sizing:border-box;margin:0;padding:0}
html,body{width:965px;height:1200px;overflow:hidden}
body{background:var(--linen);font-family:"Open Sans",Arial,sans-serif;color:var(--ink);position:relative}
.page{position:absolute;left:94px;top:0;width:771px;height:1167px;background:var(--page)}
.abs{position:absolute}

/* header */
.brand{left:0;top:14px;display:flex;align-items:center;gap:8px}
.brand-mark{width:47px;height:70px;background:var(--rust)}
.brand-name{font-size:24px;font-weight:400;color:var(--brown);line-height:1}
.brand-tag{font-size:13px;color:var(--brown);margin-top:6px;letter-spacing:1px}
.top-links{right:5px;top:25px;font-size:10px;color:var(--brown)}
.top-links span{margin:0 4px}
.cart-info{right:7px;top:55px;font-size:10px;color:var(--brown)}

/* nav */
.nav{left:0;top:110px;width:771px;height:33px;border-top:1px dotted #999;border-bottom:4px solid var(--brown);display:flex;font-size:10px;color:var(--ink)}
.nav a{display:block;padding-top:12px;text-align:center;border-right:1px dotted #555;color:inherit;text-decoration:none;height:29px}
.nav a:first-child{border-top:2px solid var(--brown);padding-top:10px}
.nav .search{margin-left:auto;width:30px;padding-top:6px}

/* hero */
.hero{left:0;top:147px;width:771px;height:335px;background:linear-gradient(115deg,#c98a5a 0%,#d7c7a2 30%,#e6d5a6 55%,#f2ead8 80%,#cbb48a 100%)}
.cap1{left:0;top:145px;width:165px;height:46px;background:rgba(70,40,20,.75);color:#fff;font-family:"Great Vibes",cursive;font-size:36px;padding:0 10px;line-height:48px}
.cap2{left:0;top:195px;width:265px;height:46px;background:rgba(70,40,20,.75);color:#fff;font-size:28px;font-weight:600;padding-left:13px;line-height:46px}
.arrows{left:722px;top:297px;width:44px;height:32px;background:#1a1a1a;display:flex;align-items:center;justify-content:center}

.quote{left:27px;top:490px;width:733px;font-family:"Italianno",cursive;font-size:30px;line-height:26px;color:#333;text-align:justify}

/* section heads */
.head{font-size:17px;color:var(--red);display:flex;align-items:center;gap:8px;font-weight:400;white-space:nowrap}
.head::after{content:"";flex:1;border-top:1px dotted #888}

/* product cards */
.card{width:253px;height:121px;background:var(--card)}
.card .title{position:absolute;left:5px;top:9px;font-size:14.5px;line-height:17px;color:#333}
.card .price{position:absolute;left:6px;top:50px;font-size:14px;font-weight:700;letter-spacing:1px}
.card .shot{position:absolute;left:145px;top:9px;width:97px;height:97px}
.btn{position:absolute;height:27px;width:101px;border-radius:3px;background:linear-gradient(var(--orange1),var(--orange2));color:#fff;font-size:10.5px;font-weight:600;display:flex;align-items:center;gap:8px;padding-left:10px}
.info{position:absolute;width:28px;height:27px;background:#fff;border:1px solid #ccc;border-radius:3px;color:#aaa;font:italic 700 16px Georgia,serif;text-align:center;line-height:25px}

/* sidebar */
.side{left:553px;top:577px;width:205px;height:303px;background:var(--side);padding:12px 10px}
.side h3{font-size:19px;font-weight:400;line-height:20px;color:var(--red)}
.side h3 span{display:block;color:#333}
.side .lead{font-size:10px;font-weight:700;color:var(--red);margin-top:6px}
.side p{font-size:10px;line-height:13.5px;color:#444}
.more{display:inline-block;background:#fff;border:1px solid #bbb;font-size:10px;padding:5px 6px;color:#333;margin-top:8px}
.ev{font-size:9.5px;line-height:12px;color:#222}
.ev b{color:var(--red);font-weight:600}

/* bottom box */
.box{left:6px;top:931px;width:758px;height:222px;border:1px solid var(--red)}
.box .divider{position:absolute;left:333px;top:10px;width:1px;height:200px;background:#666}
.feat-title{font-size:14.5px;color:#333;line-height:19px}
.feat-title b{font-size:14px;letter-spacing:1px}
.why p{font-size:10px;line-height:17.7px;color:#222}

.footer{left:0;top:1167px;width:965px;height:33px;background:var(--rust);color:#fff;font-size:9.5px;text-align:center;line-height:42px}
</style>
</head>
<body>
<div class="page">
  <header>
    <div class="abs brand">
      <div class="brand-mark"></div>
      <div>
        <div class="brand-name">Tidewell Botanics</div>
        <div class="brand-tag">organic soap</div>
      </div>
    </div>
    <div class="abs top-links">Login in <span>|</span> Checkout <span>|</span> Shopping Cart <span>|</span> My Account</div>
    <div class="abs cart-info">My cart: &nbsp;&nbsp; 1 item(s) &nbsp;| &nbsp;$ 270 (USD)</div>
  </header>

  <nav class="abs nav">
    <a style="width:54px">HOME</a>
    <a style="width:67px">SHOP</a>
    <a style="width:60px">SOAPS</a>
    <a style="width:96px">ONE FOR ONE</a>
    <a style="width:89px">SKIN FACTS</a>
    <a style="width:73px">ABOUT</a>
    <a style="width:72px">CONTACT</a>
    <span class="search"><svg width="20" height="18" viewBox="0 0 20 18"><circle cx="7" cy="7" r="5" fill="none" stroke="#222" stroke-width="2.4"/><line x1="11" y1="11" x2="18" y2="16" stroke="#222" stroke-width="3.4" stroke-linecap="round"/></svg></span>
  </nav>

  <section class="abs hero" role="img" aria-label="Photo of handmade soap bars tied with twine, a jar of rose petals, a woven ball and a lit candle on a bamboo mat">
    <div class="abs cap1">High End</div>
    <div class="abs cap2">Luxury Organic</div>
    <div class="abs arrows">
      <svg width="34" height="18" viewBox="0 0 34 18"><polyline points="10,2 4,9 10,16" fill="none" stroke="#fff" stroke-width="3"/><polyline points="24,2 30,9 24,16" fill="none" stroke="#fff" stroke-width="3"/></svg>
    </div>
  </section>

  <p class="abs quote">Lorem Ipsum is simply dummy text of the printing and typesetting industry. Lorem Ipsum has been the industry's standard dummy text ever since the 1500s.</p>

  <h2 class="abs head" style="left:7px;top:572px;width:548px">Our Products</h2>

  <div class="abs card" style="left:8px;top:621px">
    <div class="title">Skin Care Products<br>Name here</div><div class="price">$ 19</div>
    <div class="shot" role="img" aria-label="Pale yellow soap bars" style="background:linear-gradient(135deg,#efe49a,#d9cd74)"></div>
    <div class="btn" style="left:4px;top:78px"><svg width="20" height="15" viewBox="0 0 20 15"><path d="M1 2h3l2 8h10l2-6H6" fill="none" stroke="#fff" stroke-width="2"/><circle cx="8" cy="13" r="1.5" fill="#fff"/><circle cx="15" cy="13" r="1.5" fill="#fff"/></svg>Add to cart</div>
    <div class="info" style="left:108px;top:78px">i</div>
  </div>
  <div class="abs card" style="left:286px;top:619px">
    <div class="title">Skin Care Products<br>Name here</div><div class="price">$ 19</div>
    <div class="shot" role="img" aria-label="Lavender grey soap bars" style="background:linear-gradient(135deg,#8a8496,#5e586a)"></div>
    <div class="btn" style="left:4px;top:78px"><svg width="20" height="15" viewBox="0 0 20 15"><path d="M1 2h3l2 8h10l2-6H6" fill="none" stroke="#fff" stroke-width="2"/><circle cx="8" cy="13" r="1.5" fill="#fff"/><circle cx="15" cy="13" r="1.5" fill="#fff"/></svg>Add to cart</div>
    <div class="info" style="left:108px;top:78px">i</div>
  </div>
  <div class="abs card" style="left:9px;top:765px">
    <div class="title">Skin Care Products<br>Name here</div><div class="price">$ 19</div>
    <div class="shot" role="img" aria-label="Taupe oatmeal soap bars" style="background:linear-gradient(135deg,#a89c87,#8d806b)"></div>
    <div class="btn" style="left:4px;top:78px"><svg width="20" height="15" viewBox="0 0 20 15"><path d="M1 2h3l2 8h10l2-6H6" fill="none" stroke="#fff" stroke-width="2"/><circle cx="8" cy="13" r="1.5" fill="#fff"/><circle cx="15" cy="13" r="1.5" fill="#fff"/></svg>Add to cart</div>
    <div class="info" style="left:108px;top:78px">i</div>
  </div>
  <div class="abs card" style="left:286px;top:762px">
    <div class="title">Skin Care Products<br>Name here</div><div class="price">$ 19</div>
    <div class="shot" role="img" aria-label="Honey speckled soap bars" style="background:linear-gradient(135deg,#c59f6c,#a57d4d)"></div>
    <div class="btn" style="left:4px;top:78px"><svg width="20" height="15" viewBox="0 0 20 15"><path d="M1 2h3l2 8h10l2-6H6" fill="none" stroke="#fff" stroke-width="2"/><circle cx="8" cy="13" r="1.5" fill="#fff"/><circle cx="15" cy="13" r="1.5" fill="#fff"/></svg>Add to cart</div>
    <div class="info" style="left:108px;top:78px">i</div>
  </div>

  <aside class="abs side">
    <h3>New<span>Releases</span></h3>
    <div class="lead">Lorem Ipsum is simply dummy.</div>
    <p style="margin-top:4px">when an unknown printer took a galley of type and scra mbled it to make type specimen book.</p>
    <span class="more">Read more</span>
    <h3 style="margin-top:18px">Upcoming<span>Events</span></h3>
    <p class="ev" style="margin-top:3px"><b>Begins:</b> &nbsp; Saturday, March 16, 2013 at 10:00 AM EDT<br><b>Location:</b> 2184 Alder Lane Fernbrook, KY 40017</p>
    <span class="more">Read more</span>
  </aside>

  <h2 class="abs head" style="left:8px;top:904px;width:328px">Featured Products</h2>
  <h2 class="abs head" style="left:350px;top:904px;width:395px">Why Choose Our Products</h2>

  <section class="abs box">
    <div class="abs" role="img" aria-label="Two kraft soap boxes" style="left:8px;top:34px;width:130px;height:90px;background:linear-gradient(135deg,#b8946a,#96744d);border-radius:2px"></div>
    <div class="abs" style="left:155px;top:45px;width:170px">
      <div class="feat-title">Skin Care Products<br>Price <b>$ 19</b></div>
      <div style="font-size:10px;font-weight:700;color:var(--red);margin-top:4px">Lorem Ipsum is simply dummy.</div>
      <p style="font-size:10px;line-height:14px;color:#444;margin-top:2px">when an unknown printer took a galley of type and scra mbled it to make type specimen book.</p>
    </div>
    <div class="btn" style="left:11px;top:139px"><svg width="20" height="15" viewBox="0 0 20 15"><path d="M1 2h3l2 8h10l2-6H6" fill="none" stroke="#fff" stroke-width="2"/><circle cx="8" cy="13" r="1.5" fill="#fff"/><circle cx="15" cy="13" r="1.5" fill="#fff"/></svg>Add to cart</div>
    <div class="info" style="left:115px;top:139px">i</div>
    <div class="abs" style="left:160px;top:160px;font-size:10px;color:#333">Read more</div>
    <div class="divider"></div>
    <div class="abs" role="img" aria-label="Soap bar tied with ribbon beside pink daisies and a candle on pebbles" style="left:353px;top:21px;width:127px;height:127px;background:linear-gradient(135deg,#6f5b4f,#b89aa8 55%,#5a4a40)"></div>
    <div class="abs" style="left:353px;top:163px;font-size:10.5px;font-weight:700;color:var(--red)">Learn More</div>
    <div class="abs why" style="left:499px;top:23px;width:252px">
      <p style="color:var(--red);font-weight:700">Your Title Line goes Here.</p>
      <p><b>Lorem Ipsum is simply dummy text of the printing and typesetting industry. Lorem Ipsum has been the industry's standard dummy text ever since the 1500s,</b> when an unknown printer took a galley of type and scrambled it to make a type specimen book. It has survived not only five centuries, but also the leap into electronic typesetting, remaining essentially unchanged.</p>
    </div>
  </section>
</div>
<footer class="abs footer">© 2014 Copyright tidewell organic soap.</footer>
</body>
</html>
```